We need a business card design for a new soccer program based in Melbourne, Victoria, Australia.
Coaching kids from 2 through to 14 develop social, motor and soccer skills, in a fun and friendly non-competitive environment.
Our company colours are blue and orange as seen in the logo attached below. However, we are happy for the font to be any modern colour that looks professional.
Target Market(s)
Mums and dads
Industry/Entity Type
Business
Contact Information for Business Card
business name: Bright Kick Soccer
Marko Delvino Director- 0451 738 015
Luke Ferrano Director- 0419 856 371
Tomas Kovalenko Head Coach
email: marko@brightkicksoccer.com.au
website: www.brightkicksoccer.com.au
Coaching kids from 2-14
https://www.facebook.com/brightkicksoccer (facebook page not required unless it looks good without being clustered)
Look and feel

```html
<!DOCTYPE html>
<html lang="en">
<head>
<meta charset="utf-8">
<title>Bright Kick Soccer – Business Card</title>
<link rel="stylesheet" href="https://fonts.googleapis.com/css2?family=Exo+2:wght@400;500;800&display=swap">
<style>
  :root {
    --brand-orange: #f7941d;
    --brand-blue: #1f1f9e;
    --ink: #2b2b2b;
    --card: #ffffff;
    --backdrop-top: #e4e4e6;
    --backdrop-bottom: #c9c9cc;
  }
  * { box-sizing: border-box; margin: 0; padding: 0; }
  html, body { width: 1200px; height: 902px; overflow: hidden; }
  body {
    background: linear-gradient(180deg, var(--backdrop-top), var(--backdrop-bottom));
    font-family: "Exo 2", sans-serif;
    color: var(--ink);
    position: relative;
  }
  .card {
    position: absolute;
    left: 320px;
    width: 560px;
    height: 320px;
    background: var(--card);
    box-shadow: 0 6px 18px rgba(0,0,0,0.18);
  }
  .card--front { top: 96px; display: flex; align-items: center; justify-content: center; }
  .card--back { top: 476px; }

  .brand {
    display: flex;
    align-items: center;
    gap: 10px;
    font-weight: 800;
    color: var(--brand-orange);
    letter-spacing: 0.5px;
    text-transform: uppercase;
    line-height: 1;
    white-space: nowrap;
  }
  .brand__dot {
    width: 22px; height: 22px;
    border-radius: 50%;
    background: var(--brand-blue);
    flex: none;
  }
  .card--front .brand { font-size: 34px; }
  .card--back .brand {
    position: absolute;
    right: 40px;
    top: 70px;
    font-size: 30px;
  }

  .holder { position: absolute; left: 34px; top: 168px; }
  .holder__name { font-size: 19px; font-weight: 500; letter-spacing: 0.8px; text-transform: uppercase; }
  .holder__role { font-size: 13px; margin-top: 2px; }

  .contacts {
    position: absolute;
    left: 34px;
    top: 222px;
    display: grid;
    grid-template-columns: 190px auto;
    row-gap: 9px;
    column-gap: 18px;
    font-size: 12.5px;
    line-height: 1.2;
  }
  .contacts__item { display: flex; align-items: center; gap: 7px; white-space: nowrap; }
  .contacts__item--wide { grid-column: 1 / -1; }
  .contacts__icon { width: 13px; height: 13px; fill: var(--brand-orange); flex: none; }

  .band {
    position: absolute;
    left: 0; right: 0; bottom: 0;
    height: 9px;
    background: var(--brand-blue);
  }
</style>
</head>
<body>

<section class="card card--front" aria-label="Card front">
  <div class="brand"><span class="brand__dot"></span>Bright Kick Soccer</div>
</section>

<section class="card card--back" aria-label="Card back">
  <div class="brand"><span class="brand__dot"></span>Bright Kick Soccer</div>

  <div class="holder">
    <p class="holder__name">Daniel Ashford</p>
    <p class="holder__role">Managing Director</p>
  </div>

  <div class="contacts">
    <div class="contacts__item contacts__item--wide">
      <svg class="contacts__icon" viewBox="0 0 24 24"><path d="M12 1a8 8 0 0 0-8 8c0 6 8 14 8 14s8-8 8-14a8 8 0 0 0-8-8zm0 11a3 3 0 1 1 0-6 3 3 0 0 1 0 6z"/></svg>
      412 Level 3, Riverside Park Road NTH
    </div>
    <div class="contacts__item">
      <svg class="contacts__icon" viewBox="0 0 24 24"><path d="M6.6 10.8a15 15 0 0 0 6.6 6.6l2.2-2.2a1 1 0 0 1 1-.25 11.4 11.4 0 0 0 3.6.57 1 1 0 0 1 1 1V20a1 1 0 0 1-1 1A17 17 0 0 1 3 4a1 1 0 0 1 1-1h3.5a1 1 0 0 1 1 1c0 1.250.2 2.450.57 3.6a1 1 0 0 1-.25 1z"/></svg>
      045 210 3364
    </div>
    <div class="contacts__item">
      <svg class="contacts__icon" viewBox="0 0 24 24"><path d="M2 5h20v14H2zm2 2v.5l8 5 8-5V7l-8 5z"/></svg>
      name@yourmail.example
    </div>
    <div class="contacts__item">
      <svg class="contacts__icon" viewBox="0 0 24 24"><path d="M7 1h10a2 2 0 0 1 2 2v18a2 2 0 0 1-2 2H7a2 2 0 0 1-2-2V3a2 2 0 0 1 2-2zm0 3v14h10V4zm5 15.5a1 1 0 1 0 0 2 1 1 0 0 0 0-2z"/></svg>
      047 981 2205
    </div>
    <div class="contacts__item">
      <svg class="contacts__icon" viewBox="0 0 24 24"><path d="M12 2a10 10 0 1 0 0 20 10 10 0 0 0 0-20zm6.9 9h-3a15 15 0 0 0-1.3-5.5A8 8 0 0 1 18.9 11zM12 4.1c.9 1.2 1.8 3.6 2 6.9h-4c.2-3.3 1.1-5.7 2-6.9zM9.4 5.5A15 15 0 0 0 8.1 11h-3a8 8 0 0 1 4.3-5.5zM5.1 13h3a15 15 0 0 0 1.3 5.5A8 8 0 0 1 5.1 13zm6.9 6.9c-.9-1.2-1.8-3.6-2-6.9h4c-.2 3.3-1.1 5.7-2 6.9zm2.6-1.4a15 15 0 0 0 1.3-5.5h3a8 8 0 0 1-4.3 5.5z"/></svg>
      www.yoursitename.example
    </div>
  </div>

  <div class="band"></div>
</section>

</body>
</html>
```